Brixel Information Technology Solutions
We are an Information Technology Company. We provide computer services to commercial companies. We would like a new card full color front and back with bleeding edge.
We have a logo that you can use or if you want to come up with a new logo that is fine too.
Our colors are mostly Maroon and black but be creative.
Sample Information
Grant P Oswick
4818 W Saguaro Ridge Drive
Suite 410
Phoenix, AZ 85016
O: 602.555.0143
C: 602.555.0178
24/7: 888.555.0162
goswick@brixelit.com
www.brixelit.com
Target Market(s)
Business of all sizes
Industry/Entity Type
Computer
Requirements
Must have
- Bleeding edge
full color on both sides

```html
<!DOCTYPE html>
<html lang="en">
<head>
<meta charset="utf-8">
<title>Brixel Information Technology Solutions – Business Card</title>
<link rel="stylesheet" href="https://fonts.googleapis.com/css2?family=Michroma&family=Questrial&display=swap">
<style>
  :root {
    --page-bg: #e4e5e7;
    --card-bg: #f4f4f5;
    --card-shade: #e6e6e8;
    --maroon: #b3201f;
    --red-light: #e96a5c;
    --ink: #2b2b2b;
    --ink-soft: #555555;
    --faint-mark: #ead6cf;
  }
  * { box-sizing: border-box; margin: 0; padding: 0; }
  html, body {
    width: 1200px; height: 960px; overflow: hidden;
    background: var(--page-bg);
  }
  .canvas { position: relative; width: 1200px; height: 960px; }

  .card {
    position: absolute;
    width: 620px; height: 354px;
    background: radial-gradient(ellipse at 55% 40%, #ffffff 0%, var(--card-bg) 55%, var(--card-shade) 100%);
    box-shadow: 0 6px 18px rgba(0,0,0,0.18);
    overflow: hidden;
  }
  .card--front { left: 60px; top: 60px; }
  .card--back  { left: 520px; top: 546px; }

  .stripe-band {
    position: absolute; left: 0; right: 0; bottom: 0; height: 70px;
    background:
      repeating-linear-gradient(180deg, rgba(255,255,255,0) 0 4px, rgba(255,255,255,0.55) 4px 5px),
      linear-gradient(90deg, rgba(233,106,92,0.35) 0%, var(--maroon) 45%, var(--red-light) 75%, rgba(233,106,92,0.3) 100%);
    -webkit-mask-image: linear-gradient(180deg, transparent 0%, #000 45%, #000 80%, transparent 100%);
    mask-image: linear-gradient(180deg, transparent 0%, #000 45%, #000 80%, transparent 100%);
  }
  .card--front .stripe-band { bottom: 10px; height: 50px; }
  .card--back .stripe-band { bottom: 22px; height: 60px; }

  .brand {
    position: absolute; display: flex; align-items: center; gap: 10px;
    font-family: "Michroma", sans-serif; color: var(--ink);
  }
  .brand__square { background: var(--maroon); flex: none; }
  .brand__name { line-height: 1.15; }
  .brand__name strong { display: block; font-weight: 400; }
  .brand__name span { display: block; white-space: nowrap; }

  .card--front .brand { left: 30px; top: 50px; }
  .card--front .brand__square { width: 36px; height: 36px; }
  .card--front .brand__name strong { font-size: 30px; letter-spacing: 1px; }
  .card--front .brand__name span { font-size: 8px; letter-spacing: 0.5px; }

  .address {
    position: absolute; right: 40px; top: 38px;
    font-family: "Michroma", sans-serif; font-size: 10px; line-height: 1.55;
    color: var(--ink-soft); font-style: normal;
  }

  .name-rule { position: absolute; height: 1.5px; background: var(--maroon); }
  .name-rule--top { left: 150px; right: 110px; top: 130px; }
  .name-rule--bottom { left: 150px; right: 110px; top: 182px; }
  .person-name {
    position: absolute; left: 0; right: 0; top: 137px; text-align: center;
    font-family: "Questrial", sans-serif; font-weight: 400; font-size: 32px; letter-spacing: 1px; color: var(--ink);
  }

  .contacts {
    position: absolute; left: 210px; top: 194px; list-style: none;
    font-family: "Michroma", sans-serif; font-size: 10.5px; line-height: 17px; color: var(--ink-soft);
  }
  .contacts li { display: flex; align-items: center; gap: 8px; }
  .contacts svg { width: 12px; height: 12px; flex: none; }
  .contacts .no-icon { padding-left: 20px; }

  .card--back .brand { left: 36px; top: 92px; }
  .card--back .brand__square { width: 56px; height: 56px; }
  .card--back .brand__name strong { font-size: 44px; letter-spacing: 1px; }
  .card--back .brand__name span { font-size: 10px; letter-spacing: 0.3px; }

  .faint-square {
    position: absolute; right: 24px; top: 70px; width: 160px; height: 170px;
    background: var(--faint-mark); border-radius: 10px; opacity: 0.75;
  }
  .website {
    position: absolute; left: 40px; bottom: 96px;
    font-family: "Michroma", sans-serif; font-size: 18px; letter-spacing: 2px; color: var(--ink);
  }
</style>
</head>
<body>
<main class="canvas">

  <section class="card card--front" aria-label="Card front">
    <div class="brand">
      <div class="brand__square"></div>
      <div class="brand__name"><strong>BRIXEL</strong><span>INFORMATION TECHNOLOGY SOLUTIONS</span></div>
    </div>

    <address class="address">
      4818 W Saguaro Ridge Drive<br>
      Suite 410<br>
      Phoenix, AZ 85016
    </address>

    <div class="name-rule name-rule--top"></div>
    <h1 class="person-name">Grant P Oswick</h1>
    <div class="name-rule name-rule--bottom"></div>

    <ul class="contacts">
      <li>
        <svg viewBox="0 0 12 12" aria-hidden="true"><circle cx="6" cy="6" r="5.3" fill="none" stroke="#555" stroke-width="0.9"/><path d="M4.2 3.3c.4-.3.7-.2.9.2l.4.7c.1.3 0 .5-.2.7-.2.2-.2.4 0 .7.3.4.6.7 1 1 .3.2.5.2.7 0 .2-.2.4-.3.7-.2l.7.4c.4.2.5.5.2.9-.5.6-1.300.7-2.100.2C5.5 7.2 4.8 6.5 4.2 5.500c-.4-.8-.4-1.600 0-2.200z" fill="#555"/></svg>
        602.555.0143
      </li>
      <li class="no-icon">602.555.0178</li>
      <li>
        <svg viewBox="0 0 12 12" aria-hidden="true"><circle cx="6" cy="6" r="5.3" fill="none" stroke="#555" stroke-width="0.9"/><text x="6" y="7.4" text-anchor="middle" font-size="3.6" font-family="sans-serif" fill="#555">24/7</text></svg>
        888.555.0162
      </li>
      <li>
        <svg viewBox="0 0 12 12" aria-hidden="true"><circle cx="6" cy="6" r="5.3" fill="none" stroke="#555" stroke-width="0.9"/><rect x="3.3" y="4.2" width="5.4" height="3.8" fill="none" stroke="#555" stroke-width="0.7"/><path d="M3.3 4.2 6 6.3 8.7 4.2" fill="none" stroke="#555" stroke-width="0.7"/></svg>
        goswick@brixelit.com
      </li>
    </ul>

    <div class="stripe-band"></div>
  </section>

  <section class="card card--back" aria-label="Card back">
    <div class="faint-square"></div>
    <div class="brand">
      <div class="brand__square"></div>
      <div class="brand__name"><strong>BRIXEL</strong><span>INFORMATION TECHNOLOGY SOLUTIONS</span></div>
    </div>
    <p class="website">WWW.BRIXELIT.COM</p>
    <div class="stripe-band"></div>
  </section>

</main>
</body>
</html>
```